Railroad Association needs One-Page Infographic

Please see attachment for text and graphic. email with questions please. This piece will be handed out to legislators and state officials.

Target Market(s)

state legislature. state officials

Font styles to use
Serif

Colors
ec1f27

Requirements
Must have
• The graphic needs to be done right. Please email me with any questions.

```html
<!DOCTYPE html>
<html lang="en">
<head>
<meta charset="utf-8">
<title>Crossing Railroad Right of Way</title>
<link href="https://fonts.googleapis.com/css2?family=Raleway:wght@400;500;600;700;800&display=swap" rel="stylesheet">
<style>
:root{
  --red:#ec1f27;
  --red-dark:#a8151b;
  --navy:#121a45;
  --white:#ffffff;
  --stage:#e6e6e6;
  --orange:#f7a623;
  --yellow:#fbd34a;
  --teal:#12a9ad;
  --ink:#2b2b2b;
}
*{box-sizing:border-box;margin:0;padding:0}
html,body{width:1200px;height:737px;overflow:hidden;background:var(--stage);font-family:"Raleway",sans-serif}
.canvas{position:relative;width:1200px;height:737px}

/* left sheet */
.sheet{position:absolute;top:22px;height:692px;background:var(--white);overflow:hidden}
.sheet--process{left:34px;width:536px}
.hazard{position:absolute;left:0;width:100%;height:13px;
  background:repeating-linear-gradient(-45deg,#111 0 6px,var(--red) 6px 12px)}
.hazard--top{top:0}
.hazard--bottom{bottom:0}
.masthead{position:absolute;top:13px;left:0;width:100%;height:112px;
  background:linear-gradient(90deg,var(--red-dark),var(--red) 45%,var(--red));
  color:var(--white);text-align:center}
.masthead__title{font-size:42px;font-weight:600;line-height:1;margin-top:14px;letter-spacing:.5px}
.masthead__sub{font-size:32px;font-weight:400;line-height:1;margin-top:9px;letter-spacing:1px}
.question{position:absolute;top:128px;width:100%;text-align:center;color:var(--red);font-size:35px;font-weight:800}
.warm-band{position:absolute;left:0;bottom:13px;width:100%;height:152px;
  background:linear-gradient(180deg,var(--orange),var(--yellow))}
.steps{position:absolute;left:16px;top:222px;width:226px;height:368px;background:var(--navy);
  box-shadow:0 6px 8px rgba(0,0,0,.2)}
.steps__tab{position:absolute;left:16px;top:182px;width:244px;height:40px;background:var(--red);
  clip-path:polygon(0 0,100% 0,92% 50%,100% 100%,0 100%);color:var(--white);
  font-size:26px;font-weight:800;padding:4px 14px}
.steps__list{list-style:none;color:var(--white);font-size:14.3px;line-height:18.4px;padding:11px 10px 0 12px;counter-reset:s}
.steps__list li{position:relative;padding-left:16px;margin-bottom:8px;counter-increment:s}
.steps__list li::before{content:counter(s) ".";position:absolute;left:0}
.diagram{position:absolute;left:266px;top:196px;width:254px;height:254px;border-radius:6px;
  background:var(--teal);box-shadow:2px 2px 0 #0c6f72}
.callout{position:absolute;left:268px;top:472px;width:252px;height:102px;background:var(--red);
  clip-path:polygon(0 0,100% 0,100% 100%,0 100%,12% 50%);border-radius:4px;
  color:var(--white);font-size:11.6px;font-weight:700;line-height:16.4px;padding:10px 10px 0 40px}
.footnote{position:absolute;left:34px;top:610px;width:470px;font-size:11.6px;line-height:14.6px;color:var(--ink)}

/* right sheet */
.sheet--keys{left:630px;width:536px}
.photo{position:absolute;left:0;top:78px;width:536px;height:472px;
  background:linear-gradient(180deg,#5f7a4a 0%,#8a8f8a 22%,#6e6b68 55%,#4a4846 100%)}
.keys-panel{position:absolute;left:20px;top:0;width:272px;height:390px;background:rgba(18,26,69,.93)}
.keys-band{position:absolute;left:0;top:31px;width:536px;height:47px;
  background:linear-gradient(90deg,var(--red-dark),var(--red) 40%);color:var(--white);
  font-size:24px;font-weight:600;padding:10px 0 0 29px;letter-spacing:.3px}
.keys{position:absolute;left:20px;top:100px;list-style:none}
.keys li{display:flex;align-items:center;height:47px;color:var(--white);font-size:27px;font-weight:600}
.keys svg{width:60px;height:33px;margin-right:10px;flex:none}
.brand{position:absolute;left:32px;top:572px;width:130px;color:var(--navy);
  font-size:17px;font-weight:600;line-height:21px;letter-spacing:1.5px;text-transform:uppercase}
.phone{position:absolute;left:174px;top:566px;width:362px;height:94px;
  background:linear-gradient(180deg,var(--red),var(--red-dark));color:var(--white);
  font-size:48px;font-weight:700;display:flex;align-items:center;justify-content:center;letter-spacing:1px}
</style>
</head>
<body>
<div class="canvas">

  <section class="sheet sheet--process">
    <div class="hazard hazard--top"></div>
    <header class="masthead">
      <h1 class="masthead__title">Crossing Railroad</h1>
      <p class="masthead__sub">RIGHT OF WAY (ROW)</p>
    </header>
    <h2 class="question">“What is the process?”</h2>
    <div class="warm-band"></div>
    <div class="steps">
      <ol class="steps__list">
        <li>Contact railroad to obtain application and specifications.</li>
        <li>Submit application to railroad with engineering plans.</li>
        <li>When plans are approved, enter into license agreement with railroad.</li>
        <li>With railroad safety protocols and approval work plan in place, coordinate with operations to obtain flagman.</li>
      </ol>
    </div>
    <div class="steps__tab">Process:</div>
    <div class="diagram" role="img" aria-label="Diagram of a roadway with broadband expansion crossing railroad tracks within the railroad right of way"></div>
    <div class="callout">Every railroad company has a detailed process to ensure SAFETY and avoid interruption to operations when crossing railroad ROW</div>
    <p class="footnote">Railroads adhere to strict safety and notification standards so that both the entity creating an encumbrance on railroad property as well as the railroads themselves, establish clear rules of engagement that allow each to accomplish their own goals while minimizing risk to the public.</p>
    <div class="hazard hazard--bottom"></div>
  </section>

  <section class="sheet sheet--keys">
    <div class="photo" role="img" aria-label="Photograph of converging railroad tracks on gravel ballast with trees behind"></div>
    <div class="keys-panel"></div>
    <div class="keys-band">Keys to a safe and thorough process</div>
    <ul class="keys">
      <li><svg viewBox="0 0 60 33"><path d="M0 0H48L60 16.5 48 33H0Z" fill="#fff"/><g stroke="#121a45" stroke-width="2" fill="none"><path d="M22 24 L30 14 L38 20"/><path d="M20 10l4 4M24 10l-4 4M36 8l4 4M40 8l-4 4"/></g></svg>Plan</li>
      <li><svg viewBox="0 0 60 33"><path d="M0 0H48L60 16.5 48 33H0Z" fill="#fff"/><g stroke="#121a45" stroke-width="2" fill="none"><path d="M18 16.5Q30 6 42 16.5Q30 27 18 16.5Z"/><circle cx="30" cy="16.5" r="4"/></g></svg>Review</li>
      <li><svg viewBox="0 0 60 33"><path d="M0 0H48L60 16.5 48 33H0Z" fill="#fff"/><g stroke="#121a45" stroke-width="2" fill="none"><rect x="18" y="8" width="20" height="13" rx="6"/><path d="M22 21l-2 5 6-5M23 13h10M23 17h7"/></g></svg>Communicate</li>
      <li><svg viewBox="0 0 60 33"><path d="M0 0H48L60 16.5 48 33H0Z" fill="#fff"/><g stroke="#121a45" stroke-width="2" fill="none"><rect x="21" y="6" width="16" height="21"/><path d="M25 12h8M25 16h8M25 20h5"/></g></svg>Agree</li>
      <li><svg viewBox="0 0 60 33"><path d="M0 0H48L60 16.5 48 33H0Z" fill="#fff"/><g stroke="#121a45" stroke-width="2" fill="none"><path d="M22 14v11h16V14M30 6v13M25 14l5 5 5-5"/></g></svg>Install</li>
    </ul>
    <div class="brand">Lakeshore Rail Association</div>
    <div class="phone">555.014.2780</div>
  </section>

</div>
</body>
</html>
```